Coralith Partners's New Branding
Anything the customer sees, we want to update
Coralith Partners's New Branding -
Creative Brief
Professional
Dorian Pelk, MCP
Director of Technology
418 West Alder Road Morton, IL 61552
dorian.pelk@coralithpt.example
www.coralithpt.example
In addition to branding our business cards, we're also looking to brand: 1) folders - two pockets w/ a slotted area on the left pocket to insert a business card 2) brochures - 8.5"x11" tri-fold brochure 3) letterhead 4) envelopes 5) sales proposal cover letter - Our logo and name - Presented to: "Customer's name" - Presented by: "our sales person(s)" - Title of presentation - our web address 6) powerpoint 7) binders (including spline) 8) cd label - Company's name we're presenting cd to - our logo and name - title of content on cd
Quote: "Our business is sustaining yours" Please layout the quote so that if we put a QR code on the back of the card in the future, it won't look out of place.

```html
<!DOCTYPE html>
<html lang="en">
<head>
<meta charset="utf-8">
<title>Coralith Partners – Sales Proposal Cover Letter</title>
<link rel="stylesheet" href="https://fonts.googleapis.com/css2?family=Tinos:wght@400;700&display=swap">
<style>
  :root {
    --backdrop: #e9e6e1;
    --green-deep: #0f4a2e;
    --green-band: #145a37;
    --green-bright: #3c9d3a;
    --green-rule: #7cc36e;
    --paper: #ffffff;
    --grey-soft: #e4e6e5;
    --grey-line: #c9cccb;
    --ink-dark: #2f3a34;
    --gold: #d9a53a;
    --gold-light: #f1d89a;
  }
  * { box-sizing: border-box; margin: 0; padding: 0; }
  html, body {
    width: 1200px; height: 866px; overflow: hidden;
    background: var(--backdrop);
    font-family: "Tinos", "Times New Roman", serif;
  }
  .cover {
    position: absolute; left: 326px; top: 40px;
    width: 547px; height: 785px;
    background: var(--paper);
    box-shadow: 0 4px 14px rgba(0,0,0,.25);
    overflow: hidden;
  }
  .band-top {
    position: absolute; left: 0; top: 0; width: 100%; height: 65px;
    background: linear-gradient(180deg, var(--green-band), var(--green-deep));
  }
  .title-area {
    position: absolute; left: 0; top: 65px; width: 100%; height: 348px;
    background: linear-gradient(180deg, #f7f8f7 0%, #ffffff 35%, #f1f2f1 100%);
    border-top: 6px solid var(--grey-line);
    border-left: 2px solid var(--green-rule);
    border-right: 2px solid var(--green-rule);
  }
  .globe-decor {
    position: absolute; right: 0; top: 0; width: 260px; height: 240px;
    background: linear-gradient(250deg, rgba(205,214,208,.7) 0%, rgba(228,233,229,.45) 45%, rgba(255,255,255,0) 100%);
  }
  .proposal-text {
    position: absolute; left: 0; top: 66px; width: 100%; text-align: center;
    color: var(--green-bright);
  }
  .proposal-title { font-size: 21px; font-weight: 700; color: var(--green-deep); }
  .presented-to { margin-top: 6px; font-size: 14px; font-weight: 700; }
  .presented-to span { font-weight: 400; }
  .date-line { margin-top: 2px; font-size: 10px; font-weight: 700; color: var(--green-deep); }
  .presented-by { margin-top: 24px; font-size: 10px; }
  .brand {
    position: absolute; left: 0; top: 262px; width: 100%;
    display: flex; align-items: center; justify-content: center; gap: 12px;
  }
  .brand-mark { width: 36px; height: 36px; border-radius: 50%; background: var(--green-deep); }
  .brand-name { font-size: 29px; font-weight: 400; color: var(--ink-dark); letter-spacing: 1px; }
  .green-rule {
    position: absolute; left: 0; top: 413px; width: 100%; height: 17px;
    background: linear-gradient(180deg, #ffffff, #e6ebe7);
    border-bottom: 3px solid var(--green-rule);
  }
  .band-media {
    position: absolute; left: 0; top: 430px; width: 100%; height: 211px;
    background: var(--green-band);
  }
  .media-frame {
    position: absolute; top: 14px; width: 250px; height: 185px;
    border: 3px solid #ffffff;
    background: linear-gradient(180deg, #ffffff 0%, #f6ecd2 35%, var(--gold-light) 60%, var(--gold) 100%);
  }
  .media-frame.left { left: 14px; }
  .media-frame.right { left: 283px; }
  .band-grey {
    position: absolute; left: 0; top: 645px; width: 100%; height: 75px;
    background: linear-gradient(180deg, #d7dad9, var(--grey-soft) 40%, #f4f5f4);
    border-top: 2px solid var(--grey-line);
  }
  .band-bottom {
    position: absolute; left: 0; top: 720px; width: 100%; height: 65px;
    background: linear-gradient(180deg, var(--green-band), var(--green-deep));
  }
  .web {
    position: absolute; left: 0; bottom: 10px; width: 100%; text-align: center;
    font-size: 9px; color: #ffffff;
  }
</style>
</head>
<body>
  <main class="cover">
    <div class="band-top"></div>

    <section class="title-area">
      <div class="globe-decor" role="img" aria-label="Faint globe decoration"></div>
      <div class="proposal-text">
        <h1 class="proposal-title">Proposal Title</h1>
        <p class="presented-to">Presented to: <span>Company's Name</span></p>
        <p class="date-line">one date year</p>
        <p class="presented-by">Presented by: &nbsp;Sales Person(s)</p>
      </div>
      <div class="brand">
        <span class="brand-mark"></span>
        <span class="brand-name">Coralith Partners</span>
      </div>
    </section>

    <div class="green-rule"></div>

    <section class="band-media">
      <div class="media-frame left" role="img" aria-label="Photo of gold rising bar chart with red growth arrow"></div>
      <div class="media-frame right" role="img" aria-label="Photo of gold rising bar chart with red growth arrow"></div>
    </section>

    <div class="band-grey" role="img" aria-label="Faint world map texture"></div>

    <footer class="band-bottom">
      <p class="web">www.coralithpt.example</p>
    </footer>
  </main>
</body>
</html>
```